Coral Meridian 6x6m trade show booth, Wall Design

Project Overview:
Our technology company is preparing for an upcoming trade show where we will showcase various products and divisions, including thermal radars, sonar, rapid deployment solutions for perimeter security, a tactical trailer, drone technology, and our new and emerging technology division. We are seeking a graphic design for our trade show walls that will tie together all these elements while staying true to our brand identity.
Objectives:
Create a cohesive and visually appealing graphic design that integrates all elements of our trade show booth.
Emphasize our company's identity by featuring our logo and utilizing our brand colours.
Maintain a minimalistic design to ensure that our stand does not appear cluttered given the numerous elements on display.
Key Information:
Design Elements:
1. Logo Integration:
Place the company logo prominently on the trade show wall to establish brand presence.
2. Color Palette:
Use our brand colours throughout the design to maintain consistency and brand recognition.
3. Minimalistic Design:
Ensure that the design is clean and minimal to avoid overwhelming visitors with too much visual information.
4. Visual Hierarchy:
Organize the elements on the wall in a way that guides the viewer's eye naturally from one section to another.

The design should convey a sense of innovation, cutting-edge technology, and professionalism. It should inspire confidence in our products and services while being approachable.
Please feel free to ask for any additional information or clarification as needed. We are looking forward to a design that effectively represents our brand and products at the trade show. Thank you for your creative input and expertise in advance.
I have attached a detailed brief in the downloads with addition text and information to give further context to our company and also the event we will be attending.
Updates

After discussions with our team, they have decided to take a different approach and have on design replicated on both walls. this design will be one image across all panels with key words across the tob as well as our logo. please see updated design breif for details.

Target Market(s)

Professionals in Defence, Government and Critical Infrastructure

Industry/Entity Type

Defence, Government and Critical Infrastructure

Font styles to use
Sans Serif

Colors
0054AA
0677BA
7BADD7
CADEEF
E8F1F8

Requirements
Must have
• My project must have clear brand awareness and utilise the wall space provided with a cohesive design. The design must be in line with the artwork requirements provided in the downloadable brief.
Nice to have
• It would be nice to have a minimalist design while still standing out
Should not have
• No clutter, any information to be diplayed in a clean and consice manner.

```html
<!DOCTYPE html>
<html lang="en">
<head>
<meta charset="utf-8">
<title>Coral Meridian – Trade Show Wall</title>
<link rel="stylesheet" href="https://fonts.googleapis.com/css2?family=Montserrat:wght@700&family=Open+Sans:wght@400&display=swap">
<style>
  :root {
    --page: #ffffff;
    --navy: #1f2f5f;
    --navy-deep: #1e2d5c;
    --sky: #3f8fd0;
    --horizon: #bfe6f7;
    --sea: #0a7fae;
    --sea-mid: #1598bd;
    --shallows: #5cc3cf;
    --sand: #b9e2e0;
    --heading: #14a9d8;
    --white: #ffffff;
  }
  * { margin: 0; padding: 0; box-sizing: border-box; }
  html, body { width: 1200px; height: 720px; overflow: hidden; background: var(--page); }
  .wall { position: relative; width: 1200px; height: 720px; }
  .edge-strip {
    position: absolute; left: 14px; top: 137px; width: 10px; height: 459px;
    background: var(--navy-deep);
  }
  .panel {
    position: absolute; top: 137px; width: 188px; height: 459px; overflow: hidden;
  }
  .panel-scene {
    position: absolute; inset: 0;
    background: linear-gradient(180deg,
      var(--navy) 0%, var(--navy) 22%, #27508f 32%, var(--sky) 40%,
      var(--horizon) 45%, #2b8ab8 47%, var(--sea) 52%, var(--sea-mid) 68%,
      var(--shallows) 82%, var(--sand) 100%);
  }
  .panel--last { top: 141px; width: 176px; }
  .panel-title {
    position: absolute; top: 20px; left: 0; right: 0; text-align: center;
    font-family: 'Montserrat', sans-serif; font-weight: 700; font-size: 16.5px;
    line-height: 16px; letter-spacing: 1.4px; color: var(--heading);
  }
  .brand-name {
    position: absolute; top: 68px; left: 0; right: 0; text-align: center;
    font-family: 'Open Sans', sans-serif; font-weight: 400; font-size: 23px;
    color: var(--white);
  }
  .brand-dot {
    position: absolute; top: 20px; left: 50%; width: 48px; height: 48px;
    margin-left: -24px; border-radius: 50%; background: var(--white);
  }
  .reticle { position: absolute; width: 100px; height: 100px; }
</style>
</head>
<body>
<main class="wall">
  <div class="edge-strip"></div>

  <section class="panel" style="left:29px">
    <div class="panel-scene" role="img" aria-label="Ocean photograph split at the waterline: night-blue sky above, clear turquoise water and sandy seabed below, with rising bubbles"></div>
    <div class="brand-dot"></div>
    <p class="brand-name">Coral Meridian</p>
  </section>

  <section class="panel" style="left:222px">
    <div class="panel-scene" role="img" aria-label="Continuation of the ocean photograph across the waterline"></div>
    <h2 class="panel-title">SOVEREIGN<br>SOLUTIONS</h2>
    <svg class="reticle" style="left:42px;top:83px" viewBox="0 0 100 100" aria-hidden="true">
      <g fill="none" stroke="#fff" stroke-width="1.6">
        <circle cx="50" cy="50" r="48"/><circle cx="50" cy="50" r="45"/><circle cx="50" cy="50" r="11"/>
        <path d="M50 5V95M5 50H95M45 20h10M45 35h10M45 65h10M45 80h10M20 45v10M35 45v10M65 45v10M80 45v10"/>
      </g>
    </svg>
  </section>

  <section class="panel" style="left:416px">
    <div class="panel-scene" role="img" aria-label="Continuation of the ocean photograph with a soft cloud on the horizon"></div>
    <h2 class="panel-title">DEPLOYABLE</h2>
  </section>

  <section class="panel" style="left:609px">
    <div class="panel-scene" role="img" aria-label="Continuation of the ocean photograph with bright sunlight at the horizon"></div>
    <h2 class="panel-title">UNDER WATER</h2>
    <svg class="reticle" style="left:45px;top:308px" viewBox="0 0 100 100" aria-hidden="true">
      <g fill="none" stroke="#fff" stroke-width="1.6">
        <circle cx="50" cy="50" r="48"/><circle cx="50" cy="50" r="45"/><circle cx="50" cy="50" r="11"/>
        <path d="M50 5V95M5 50H95M45 20h10M45 35h10M45 65h10M45 80h10M20 45v10M35 45v10M65 45v10M80 45v10"/>
      </g>
    </svg>
  </section>

  <section class="panel" style="left:802px">
    <div class="panel-scene" role="img" aria-label="Continuation of the ocean photograph with pink-tinted clouds"></div>
    <h2 class="panel-title">ON WATER</h2>
    <svg class="reticle" style="left:44px;top:182px" viewBox="0 0 100 100" aria-hidden="true">
      <g fill="none" stroke="#fff" stroke-width="1.6">
        <circle cx="50" cy="50" r="48"/><circle cx="50" cy="50" r="45"/><circle cx="50" cy="50" r="11"/>
        <path d="M50 5V95M5 50H95M45 20h10M45 35h10M45 65h10M45 80h10M20 45v10M35 45v10M65 45v10M80 45v10"/>
      </g>
    </svg>
  </section>

  <section class="panel panel--last" style="left:995px">
    <div class="panel-scene" role="img" aria-label="End of the ocean photograph with rising bubbles below the waterline"></div>
    <h2 class="panel-title">ABOVE WATER</h2>
  </section>
</main>
</body>
</html>
```